Business Cards

Business cards (double-sided) to be handed out to clients and potential clients, with contact details, logo .

Target Market(s)

Small to medium size businesses

Industry/Entity Type

Accountants

Contact Information for Business Card

Brightwater Ledger & Counsel Ltd

Colors

Designer to choose only greyscale colors for use in the design.

Requirements
Must have
• Name, Title, Address, Phone number, Email, Website
Nice to have
• Modern, clean lines, classy
Should not have
• Business cards to be double-sided. Form keeps reverting to single-sided.

```html
<!DOCTYPE html>
<html lang="en">
<head>
<meta charset="utf-8">
<title>Brightwater Ledger &amp; Counsel — Business Cards</title>
<link href="https://fonts.googleapis.com/css2?family=Montserrat:wght@400;500;600&display=swap" rel="stylesheet">
<style>
  :root {
    --backdrop: #2f2f2f;
    --card-white: #ffffff;
    --card-black: #161616;
    --card-black-soft: #1f1f1f;
    --stripe-grey: #8c8c8c;
    --ink-dark: #151515;
    --ink-light: #f4f4f4;
    --rule-grey: #555555;
  }
  * { box-sizing: border-box; margin: 0; padding: 0; }
  html, body {
    width: 1200px; height: 1200px; overflow: hidden;
    background: var(--backdrop);
    font-family: "Montserrat", sans-serif;
  }
  .sheet {
    width: 1200px; height: 1200px;
    display: flex; flex-direction: column; align-items: center; justify-content: center;
    gap: 40px;
  }
  .card {
    position: relative;
    width: 880px; height: 500px;
    border-radius: 42px;
    overflow: hidden;
    box-shadow: 0 14px 30px rgba(0,0,0,.45);
  }

  /* Front */
  .card--front { background: var(--card-white); }
  .front__brand {
    position: absolute; left: 0; right: 0; top: 0; height: 270px;
    display: flex; align-items: center; justify-content: center;
  }
  .brand-name {
    font-weight: 500;
    font-size: 40px;
    letter-spacing: 4px;
    text-transform: uppercase;
    text-align: center;
    line-height: 1.25;
  }
  .front__brand .brand-name { color: var(--ink-dark); }
  .front__stripe {
    position: absolute; left: 0; right: 0; top: 278px; height: 10px;
    background: var(--stripe-grey);
  }
  .front__band {
    position: absolute; left: 0; right: 0; top: 296px; bottom: 0;
    background: linear-gradient(100deg, var(--card-black) 0%, var(--card-black-soft) 60%, var(--card-black) 100%);
    display: flex; align-items: center;
  }
  .holder {
    width: 400px; padding-left: 60px;
    display: flex; align-items: stretch; gap: 16px;
  }
  .holder__bar { width: 5px; background: var(--ink-light); }
  .holder__name {
    color: var(--ink-light); font-weight: 600; font-size: 34px; letter-spacing: .5px; line-height: 1.1;
  }
  .holder__title {
    color: var(--ink-light); font-weight: 400; font-size: 19px; margin-top: 6px; letter-spacing: .5px;
  }
  .band__divider { width: 1px; height: 140px; background: var(--rule-grey); }
  .contacts {
    list-style: none; padding-left: 40px;
    color: var(--ink-light); font-size: 17px; line-height: 1.2;
  }
  .contacts li { display: flex; align-items: center; gap: 12px; margin: 6px 0; }
  .contacts svg { width: 20px; height: 20px; flex: none; fill: none; stroke: var(--ink-light); stroke-width: 1.8; }
  .contacts svg.solid { fill: var(--ink-light); stroke: none; }

  /* Back */
  .card--back {
    background: linear-gradient(100deg, var(--card-black) 0%, var(--card-black-soft) 55%, var(--card-black) 100%);
    display: flex; align-items: center; justify-content: center;
  }
  .card--back .brand-name { color: var(--ink-light); font-size: 46px; }
</style>
</head>
<body>
<main class="sheet">
  <section class="card card--front" aria-label="Business card front">
    <div class="front__brand">
      <p class="brand-name">Brightwater Ledger<br>&amp; Counsel</p>
    </div>
    <div class="front__stripe"></div>
    <div class="front__band">
      <div class="holder">
        <span class="holder__bar"></span>
        <div>
          <p class="holder__name">DANIEL REEVE</p>
          <p class="holder__title">CEO | FOUNDER</p>
        </div>
      </div>
      <span class="band__divider"></span>
      <ul class="contacts">
        <li>
          <svg class="solid" viewBox="0 0 24 24"><path d="M6.6 10.8a15 15 0 0 0 6.6 6.6l2.2-2.2a1 1 0 0 1 1-.25 11.4 11.4 0 0 0 3.6.57 1 1 0 0 1 1 1V20a1 1 0 0 1-1 1A17 17 0 0 1 3 4a1 1 0 0 1 1-1h3.5a1 1 0 0 1 1 1c0 1.25.2 2.45.57 3.57a1 1 0 0 1-.25 1z"/></svg>
          (555) 014 2290
        </li>
        <li>
          <svg viewBox="0 0 24 24"><rect x="3" y="5" width="18" height="14"/><path d="M3 5l9 8 9-8"/></svg>
          hello@brightwaterledger.com
        </li>
        <li>
          <svg viewBox="0 0 24 24"><circle cx="12" cy="12" r="9"/><path d="M3 12h18M12 3c3 3 3 15 0 18M12 3c-3 3-3 15 0 18"/></svg>
          www.brightwaterledger.com
        </li>
        <li>
          <svg viewBox="0 0 24 24"><path d="M12 22s7-7 7-12a7 7 0 0 0-14 0c0 5 7 12 7 12z"/><circle cx="12" cy="10" r="2.5"/></svg>
          <span>12 Harbour Lane, Easton, State<br>0421 Country</span>
        </li>
      </ul>
    </div>
  </section>

  <section class="card card--back" aria-label="Business card back">
    <p class="brand-name">Brightwater Ledger<br>&amp; Counsel</p>
  </section>
</main>
</body>
</html>
```